Environmentally conscious Waste Management Company requires business card

We Require a Business card for our environmentally conscious waste management company . The business card should have a very clean design. be double sided and incorporate our logo..
The card will need o have 9 lines for the contact details - that are
Name
Title
Business
Address Line 1
Address Line 2
Address Line 3
Phone
Mobile
Email

Industry/Entity Type

Waste Management

Other font styles liked:
• Helvetica or similar

```html
<!DOCTYPE html>
<html lang="en">
<head>
<meta charset="utf-8">
<title>tidyloop business card</title>
<link rel="stylesheet" href="https://fonts.googleapis.com/css2?family=Inter:wght@300;400&display=swap">
<style>
  :root {
    --green: #17b82e;
    --white: #ffffff;
    --paper-shade: #eeeeee;
    --ink: #3a3a3a;
    --ink-soft: #555555;
    --backdrop: #2b2b2b;
  }
  * { margin: 0; padding: 0; box-sizing: border-box; }
  html, body { width: 1200px; height: 900px; overflow: hidden; }
  body {
    background: var(--backdrop);
    font-family: "Inter", Helvetica, Arial, sans-serif;
    font-weight: 300;
    color: var(--ink);
    position: relative;
  }
  .card {
    position: absolute;
    left: 280px;
    width: 640px;
    height: 366px;
    background: linear-gradient(135deg, var(--white) 55%, var(--paper-shade));
    overflow: hidden;
    box-shadow: 0 10px 30px rgba(0,0,0,0.5);
  }
  .card--front { top: 54px; }
  .card--back { top: 480px; }
  .card__bands { position: absolute; inset: 0; width: 100%; height: 100%; }

  .brand { position: absolute; display: flex; align-items: center; gap: 10px; }
  .brand__square { width: 26px; height: 26px; background: var(--green); }
  .brand__name {
    font-weight: 400;
    color: var(--green);
    letter-spacing: -1px;
    line-height: 1;
  }
  .card--front .brand { left: 50%; top: 50%; transform: translate(-50%, -50%); }
  .card--front .brand__name { font-size: 62px; }
  .card--front .brand__square { width: 34px; height: 34px; }
  .card--back .brand { left: 40px; top: 62px; }
  .card--back .brand__name { font-size: 44px; }

  .person { position: absolute; right: 40px; top: 52px; text-align: right; }
  .person__name { font-size: 20px; letter-spacing: 0.5px; color: var(--ink); }
  .person__title { font-size: 13px; color: var(--ink-soft); margin-top: 1px; }

  .social { position: absolute; left: 420px; top: 140px; list-style: none; }
  .social li { display: flex; align-items: center; gap: 12px; height: 26px; font-size: 11px; }
  .social__mark { width: 17px; height: 17px; background: var(--green); }

  .contact { position: absolute; left: 44px; top: 226px; list-style: none; }
  .contact li { display: flex; align-items: center; gap: 14px; height: 28px; font-size: 12px; }
  .icon { width: 22px; height: 22px; fill: var(--green); flex: none; }

  .address {
    position: absolute; left: 200px; top: 318px;
    display: flex; align-items: center; gap: 10px; font-size: 12px;
  }
</style>
</head>
<body>

  <section class="card card--front" aria-label="Card front">
    <svg class="card__bands" viewBox="0 0 640 366" preserveAspectRatio="none" aria-hidden="true">
      <path d="M0 0 H540 Q560 0 575 14 H0 Z" fill="var(--green)"/>
      <path d="M0 366 V352 H560 Q585 352 600 336 Q612 326 640 326 V366 Z" fill="var(--green)"/>
    </svg>
    <div class="brand">
      <span class="brand__square"></span>
      <span class="brand__name">tidyloop</span>
    </div>
  </section>

  <section class="card card--back" aria-label="Card back">
    <svg class="card__bands" viewBox="0 0 640 366" preserveAspectRatio="none" aria-hidden="true">
      <path d="M0 0 H510 Q535 0 550 10 L560 16 H0 Z M0 0 V16 H0 Z" fill="var(--green)"/>
      <path d="M0 16 H560 Q552 24 548 24 H0 Z" fill="var(--green)" opacity="0"/>
      <path d="M640 230 V366 H130 Q150 340 190 340 H600 Q630 340 640 230 Z" fill="var(--green)"/>
      <path d="M640 244 V354 H200 Q190 354 200 354 Z" fill="var(--white)" opacity="0"/>
    </svg>
    <svg class="card__bands" viewBox="0 0 640 366" preserveAspectRatio="none" aria-hidden="true">
      <path d="M0 0 H640 V244 Q630 350 560 352 H185 Q160 352 140 366 H0 Z M0 14 V366" fill="none"/>
      <path d="M0 14 H548 Q565 14 575 0 H640 V232 Q634 338 572 340 H190 Q160 340 135 366 H0 Z" fill="var(--white)"/>
      <path d="M0 0 H575 Q565 14 548 14 H0 Z" fill="var(--green)"/>
    </svg>

    <div class="brand">
      <span class="brand__square"></span>
      <span class="brand__name">tidyloop</span>
    </div>

    <div class="person">
      <p class="person__name">YOUR NAME</p>
      <p class="person__title">Designation</p>
    </div>

    <ul class="social">
      <li><span class="social__mark"></span>@tidyloopnz</li>
      <li><span class="social__mark"></span>/tidyloop.co.nz</li>
      <li><span class="social__mark"></span>/tl-4KpR</li>
    </ul>

    <ul class="contact">
      <li>
        <svg class="icon" viewBox="0 0 24 24" aria-hidden="true"><path d="M3 8 Q12 2 21 8 L19 11 L16 10 V8 H8 V10 L5 11 Z M6 12 H18 L20 20 H4 Z"/></svg>
        00(64)3550147
      </li>
      <li>
        <svg class="icon" viewBox="0 0 24 24" aria-hidden="true"><path d="M7 2 H17 A2 2 0 0 1 19 4 V20 A2 2 0 0 1 17 22 H7 A2 2 0 0 1 5 20 V4 A2 2 0 0 1 7 2 Z M7 5 V18 H17 V5 Z"/></svg>
        00(64)225550193
      </li>
      <li>
        <svg class="icon" viewBox="0 0 24 24" aria-hidden="true"><path d="M2 5 H22 V19 H2 Z M3.5 6.5 L12 13 L20.5 6.5 Z"/></svg>
        mayalee@tidyloop.com
      </li>
    </ul>

    <div class="address">
      <svg class="icon" viewBox="0 0 24 24" aria-hidden="true"><path d="M12 2 A7 7 0 0 1 19 9 C19 14 12 22 12 22 C12 22 5 14 5 9 A7 7 0 0 1 12 2 Z M12 6 A3 3 0 1 0 12 12 A3 3 0 1 0 12 6 Z"/></svg>
      Fern Street, Ashvale, New Zealand 3120
    </div>
  </section>

</body>
</html>
```